Technical Redesign of AI-Generated Method & Topic Graphics for PowerPoint

e have a set of graphics and diagrams that were initially created using AI. The content, structure, and overall layout are already defined and should remain largely unchanged.

The objective is NOT to create completely new designs. This is primarily a technical refinement and conversion project. The graphics need to be professionally redrawn, cleaned up, and rebuilt so that they:

• Look less AI-generated and more professional/corporate
• Match our existing corporate website style
• Are fully editable in Microsoft PowerPoint
• Use consistent fonts, colors, spacing, and iconography
• Maintain the original meaning and information structure

REFERENCE WEBSITE
https://moorwald-forschung. at/

Please use the website as the primary reference for:
• Color palette
• Typography
• Visual language
• General corporate look and feel
• Professional, research-oriented appearance

The style should be clean, technical, modern, and suitable for a scientific/research institution.

SCOPE OF WORK
For each supplied graphic:

1. Recreate the graphic manually
- Do not simply trace or export the AI image.
- Rebuild all elements using PowerPoint native objects where possible.

2. Improve visual quality
- Remove typical AI-generated inconsistencies.
- Correct alignment, spacing, proportions, and visual hierarchy.
- Standardize icons and graphic elements.

3. Corporate style adaptation
- Apply colors and typography consistent with our website.
- Use a professional and technically oriented visual style.
- Avoid decorative or overly creative design elements.

4. Ensure full editability
- All text must remain editable.
- Shapes should be editable PowerPoint objects.
- Icons should preferably be vector-based.
- Elements should not be flattened into images unless absolutely necessary.

DELIVERABLES
Required output:

• Microsoft PowerPoint (.pptx)
• All graphics fully editable
• Layered and logically grouped objects
• Consistent formatting across all graphics
• Optional source files (.svg, .ai, or . eps) if available

DESIGN DIRECTION
Please focus on:

• Technical accuracy
• Professional presentation quality
• Corporate consistency
• PowerPoint usability

Please do NOT focus on:
• Creating alternative concepts
• Artistic reinterpretations
• Major layout changes
• Creative redesigns

The goal is to transform existing AI-generated diagrams into professional, corporate-standard, PowerPoint-editable graphics that fit seamlessly with the Moorwaldinstitut Graz website and presentation materials.

```html
<!DOCTYPE html>
<html lang="en">
<head>
<meta charset="utf-8">
<title>Multi-Criteria Decision Analysis (MCDA)</title>
<link href="https://fonts.googleapis.com/css2?family=Hind:wght@400;500;600;700&display=swap" rel="stylesheet">
<style>
:root{
  --navy:#1f3a7a;
  --blue:#1a73c8;
  --sky:#e1f3fc;
  --icon-fill:#c7daf0;
  --orange:#ee6b1e;
  --orange-fill:#fde3c6;
  --green:#3fae49;
  --green-dark:#277a2f;
  --green-fill:#e6f1d0;
  --text:#1b2a55;
  --page:#eeeeee;
}
*{box-sizing:border-box;margin:0;padding:0}
html,body{width:1200px;height:1200px;overflow:hidden}
body{background:var(--page);font-family:"Hind",Arial,sans-serif;color:var(--text)}
.card{position:absolute;left:0;top:175px;width:1200px;height:849px;background:#fff}
.abs{position:absolute}
.title{left:0;width:1200px;top:32px;text-align:center;font-size:37px;font-weight:700;color:var(--navy);letter-spacing:.2px}
.subtitle{left:0;width:1200px;top:83px;text-align:center;font-size:20px;font-style:italic;font-weight:500;color:var(--blue)}
.info-box{background:var(--sky);border:1.5px solid var(--navy);border-radius:8px}
.info-box h2{position:absolute;left:108px;top:14px;font-size:17px;font-weight:600;color:var(--navy)}
.info-box .icon{position:absolute;left:22px;top:20px}
ul{list-style:none}
li{position:relative;padding-left:13px;font-size:11.2px;line-height:1.3;font-weight:500;color:var(--text);margin-bottom:7px}
li::before{content:"";position:absolute;left:0;top:5px;width:4px;height:4px;border-radius:50%;background:var(--navy)}
.info-box ul{position:absolute;left:97px;top:43px;right:12px}
.step{background:#fff;border:1.5px solid var(--navy);border-radius:8px;top:336px;height:217px}
.step .num{position:absolute;left:10px;top:9px;width:27px;height:27px;border-radius:50%;background:var(--navy);color:#fff;font-size:14px;font-weight:500;display:flex;align-items:center;justify-content:center}
.step h3{position:absolute;top:13px;font-size:15.5px;font-weight:600;line-height:1.2;color:var(--navy);text-align:center}
.step .badge{position:absolute;left:8px;top:57px;width:62px;height:79px;border-radius:50%;background:var(--icon-fill);border:1.5px solid var(--navy);display:flex;align-items:center;justify-content:center}
.step ul{position:absolute;left:72px;top:60px}
.step li{margin-bottom:8px;white-space:nowrap}
.step li.tight{letter-spacing:-.35px}
.step.accent{border-color:var(--orange)}
.step.accent .num{background:var(--orange)}
.step.accent h3{color:var(--orange)}
.step.accent .badge{background:var(--orange-fill);border-color:var(--orange)}
.step.accent li::before{background:var(--orange)}
.flow-arrow{top:421px;width:0;height:0;border-top:15px solid transparent;border-bottom:15px solid transparent;border-left:14px solid var(--navy)}
.down-arrow{top:566px;width:0;height:0;border-left:10px solid transparent;border-right:10px solid transparent;border-top:9px solid var(--navy)}
.summary{left:41px;top:588px;width:1119px;height:160px;background:var(--green-fill);border:1.5px solid var(--green);border-radius:16px}
.summary .seal{position:absolute;left:52px;top:17px;width:125px;height:125px;border-radius:50%;background:#fff;border:1.5px solid var(--green);display:flex;align-items:center;justify-content:center}
.summary h2{position:absolute;left:216px;top:12px;font-size:27px;font-weight:700;color:var(--green-dark);white-space:nowrap}
.benefit{position:absolute;top:64px;display:flex;align-items:center;height:66px}
.benefit p{font-size:11.2px;line-height:1.45;font-weight:500;color:var(--text);white-space:nowrap}
.benefit svg{flex:none}
.footer-rule{top:784px;height:1.2px;background:var(--navy)}
.footer-note{left:270px;top:773px;font-size:13.5px;font-style:italic;font-weight:500;color:var(--navy)}
.brand{left:980px;top:764px;display:flex;align-items:center;gap:10px}
.brand-dot{width:46px;height:46px;border-radius:50%;border:1.5px solid var(--green-dark)}
.brand-name{font-size:15.5px;font-weight:600;line-height:1.2;color:var(--navy)}
</style>
</head>
<body>
<main class="card">
  <h1 class="abs title">Multi-Criteria Decision Analysis (MCDA)</h1>
  <p class="abs subtitle">From raw parameters to transparent technology ranking</p>

  <section class="abs info-box" style="left:41px;top:126px;width:295px;height:188px">
    <svg class="icon" width="58" height="58" viewBox="0 0 58 58" fill="none" stroke="var(--navy)" stroke-width="4">
      <circle cx="27" cy="31" r="24"/><circle cx="27" cy="31" r="15"/><circle cx="27" cy="31" r="6" fill="var(--navy)"/>
      <path d="M27 31 L50 8" stroke-width="3.5"/><path d="M44 6 L52 2 L50 12 Z" fill="var(--navy)" stroke-width="1"/>
    </svg>
    <h2>Starting Point</h2>
    <ul style="left:97px;top:42px">
      <li>Competing energy and<br>infrastructure technologies</li>
      <li>Multiple, partly conflicting<br>decision criteria</li>
      <li>Conflict of sustainability goals</li>
      <li>Need for scenario-specific and<br>transparent decision support</li>
    </ul>
  </section>

  <section class="abs info-box" style="left:360px;top:126px;width:343px;height:188px">
    <svg class="icon" style="left:18px;top:18px" width="38" height="46" viewBox="0 0 38 46" fill="var(--navy)">
      <ellipse cx="19" cy="7" rx="18" ry="6"/>
      <path d="M1 12 q18 9 36 0 v9 q-18 9 -36 0z"/>
      <path d="M1 25 q18 9 36 0 v9 q-18 9 -36 0z"/>
      <path d="M1 38 q18 9 36 0 v1 q-18 12 -36 0z"/>
    </svg>
    <h2 style="left:82px;top:13px">Methodological Foundations</h2>
    <ul style="left:76px;top:43px">
      <li>Raw input parameters and KPI definitions</li>
      <li>Representative values from realistic<br>datasets</li>
      <li>Weighting scheme and scenario<br>assumptions</li>
      <li>Literature, simulation and measurement<br>data integrated</li>
    </ul>
  </section>

  <section class="abs step" style="left:41px;width:218px">
    <span class="num">1</span>
    <h3 style="left:50px">KPI Calculation</h3>
    <div class="badge">
      <svg width="30" height="44" viewBox="0 0 30 44" fill="var(--navy)">
        <rect x="0" y="0" width="30" height="44" rx="4"/>
        <rect x="4" y="4" width="22" height="9" fill="#fff"/>
        <g fill="#fff"><rect x="4" y="17" width="5" height="5"/><rect x="12" y="17" width="5" height="5"/><rect x="20" y="17" width="6" height="5"/><rect x="4" y="25" width="5" height="5"/><rect x="12" y="25" width="5" height="5"/><rect x="20" y="25" width="6" height="13"/><rect x="4" y="33" width="5" height="5"/><rect x="12" y="33" width="5" height="5"/></g>
      </svg>
    </div>
    <ul style="left:74px;top:58px">
      <li>Derive relevant KPIs<br>from input parameters</li>
      <li>Cover technical,<br>economic, ecological,<br>social and socio-<br>economic dimensions</li>
      <li>Ensure technology-<br>specific metrics</li>
    </ul>
  </section>
  <span class="abs flow-arrow" style="left:266px"></span>

  <section class="abs step" style="left:285px;width:205px">
    <span class="num">2</span>
    <h3 style="left:62px">Normalization</h3>
    <div class="badge">
      <svg width="36" height="46" viewBox="0 0 36 46" fill="none" stroke="var(--navy)" stroke-width="2.5">
        <path d="M6 2v42M18 2v42M30 2v42"/>
        <circle cx="6" cy="26" r="4" fill="var(--icon-fill)"/><circle cx="18" cy="12" r="4" fill="var(--icon-fill)"/><circle cx="30" cy="26" r="4" fill="var(--icon-fill)"/>
      </svg>
    </div>
    <ul style="left:72px;top:58px">
      <li class="tight">Convert heterogeneous<br>KPI scales to a<br>common scale</li>
      <li class="tight">Min-max normalization<br>to 0-100</li>
      <li style="line-height:1.5">Enable consistent<br>comparison of<br>metrics</li>
    </ul>
  </section>
  <span class="abs flow-arrow" style="left:497px"></span>

  <section class="abs step" style="left:514px;width:193px">
    <span class="num">3</span>
    <h3 style="left:54px;width:130px">Weighting<br>&amp; Aggregation</h3>
    <div class="badge">
      <svg width="46" height="42" viewBox="0 0 46 42" fill="var(--navy)">
        <rect x="2" y="26" width="8" height="16"/><rect x="14" y="19" width="8" height="23"/><rect x="26" y="11" width="8" height="31"/>
        <path d="M2 20 L38 4" stroke="var(--navy)" stroke-width="3" fill="none"/><path d="M34 0 L44 2 L38 10Z"/>
      </svg>
    </div>
    <ul style="left:72px;top:70px">
      <li class="tight">Weight criteria<br>according to scenario<br>priorities</li>
      <li>Aggregate into an<br>overall score</li>
      <li>Ensure transparency<br>of assumptions</li>
    </ul>
  </section>
  <span class="abs flow-arrow" style="left:715px"></span>

  <section class="abs step accent" style="left:732px;width:207px">
    <span class="num">4</span>
    <h3 style="left:40px;width:160px">Sensitivity &amp;<br>Uncertainty Analysis</h3>
    <div class="badge">
      <svg width="46" height="40" viewBox="0 0 46 40" fill="none" stroke="var(--orange)" stroke-width="2">
        <path d="M2 36 C14 36 16 6 23 6 C30 6 32 36 44 36"/>
        <g fill="var(--orange)" stroke="none"><circle cx="8" cy="24" r="1.6"/><circle cx="14" cy="12" r="1.6"/><circle cx="20" cy="20" r="1.6"/><circle cx="24" cy="28" r="1.6"/><circle cx="30" cy="16" r="1.6"/><circle cx="36" cy="8" r="1.6"/><circle cx="38" cy="26" r="1.6"/><circle cx="18" cy="32" r="1.6"/><circle cx="28" cy="2" r="1.6"/></g>
      </svg>
    </div>
    <ul style="left:76px;top:70px">
      <li class="tight">Monte Carlo simulation<br>of uncertain inputs</li>
      <li>Test robustness<br>of results</li>
      <li>Analyze influence of<br>key assumptions and<br>weightings</li>
    </ul>
  </section>
  <span class="abs flow-arrow" style="left:946px"></span>

  <section class="abs step" style="left:965px;width:195px">
    <span class="num">5</span>
    <h3 style="left:50px;width:130px">Ranking &amp;<br>Interpretation</h3>
    <div class="badge">
      <svg width="42" height="44" viewBox="0 0 42 44" fill="var(--navy)">
        <path d="M10 2h22v14a11 11 0 0 1-22 0z"/>
        <path d="M10 6H3v5a8 8 0 0 0 8 8M32 6h7v5a8 8 0 0 1-8 8" fill="none" stroke="var(--navy)" stroke-width="3"/>
        <rect x="18" y="27" width="6" height="8"/><rect x="11" y="35" width="20" height="6"/>
        <path d="M21 6l2.2 4.5 5 .6-3.7 3.4 1 5-4.5-2.5-4.5 2.5 1-5-3.7-3.4 5-.6z" fill="#fff"/>
      </svg>
    </div>
    <ul style="left:76px;top:70px">
      <li>Rank technology<br>options</li>
      <li>Identify trade-offs<br>and hotspots</li>
      <li>Provide clear,<br>actionable insights</li>
    </ul>
  </section>

  <span class="abs down-arrow" style="left:136px"></span>
  <span class="abs down-arrow" style="left:380px"></span>
  <span class="abs down-arrow" style="left:601px"></span>
  <span class="abs down-arrow" style="left:825px"></span>
  <span class="abs down-arrow" style="left:1054px"></span>

  <section class="summary abs">
    <div class="seal">
      <svg width="74" height="90" viewBox="0 0 74 90" fill="none" stroke="var(--green)" stroke-width="4">
        <rect x="4" y="10" width="50" height="72" rx="3"/>
        <rect x="18" y="4" width="22" height="10" rx="3" fill="var(--green)"/>
        <path d="M11 28l4 4 6-8M11 44l4 4 6-8M11 60l4 4 6-8" stroke-width="3"/>
        <path d="M27 30h18M27 46h18M27 62h10" stroke-width="3.5"/>
        <circle cx="56" cy="70" r="17" fill="var(--green)" stroke="#fff" stroke-width="3"/>
        <path d="M48 70l6 6 10-11" stroke="#fff" stroke-width="4"/>
      </svg>
    </div>
    <h2>Integrated MCDA Assessment - Transparent, Robust, Decision-Ready</h2>

    <div class="benefit" style="left:207px;gap:12px">
      <svg width="54" height="50" viewBox="0 0 54 50" fill="none" stroke="var(--green)" stroke-width="2.5">
        <path d="M27 4v42M16 46h22M6 10h42M6 10l-5 16h10zM48 10l-5 16h10z"/>
        <path d="M1 26a5 4 0 0 0 10 0M43 26a5 4 0 0 0 10 0"/>
      </svg>
      <p>Structured comparison<br>of alternatives across<br>multiple dimensions</p>
    </div>
    <div class="benefit" style="left:415px;gap:12px">
      <svg width="42" height="46" viewBox="0 0 42 46" fill="none" stroke="var(--green)" stroke-width="2.5">
        <circle cx="18" cy="18" r="15"/><path d="M29 29l11 12" stroke-width="4.5"/>
        <path d="M9 18q9-8 18 0q-9 8-18 0z"/><circle cx="18" cy="18" r="2.5" fill="var(--green)"/>
      </svg>
      <p>Identification of<br>trade-offs and<br>hotspots</p>
    </div>
    <div class="benefit" style="left:570px;gap:12px">
      <svg width="36" height="48" viewBox="0 0 36 48" fill="none" stroke="var(--green)" stroke-width="2.5">
        <path d="M18 2L3 8v14c0 12 7 20 15 24 8-4 15-12 15-24V8z"/><path d="M10 24l6 6 11-12" stroke-width="3"/>
      </svg>
      <p>Robust results<br>under uncertainty<br>and sensitivity</p>
    </div>
    <div class="benefit" style="left:732px;gap:10px">
      <svg width="38" height="32" viewBox="0 0 38 32" fill="none" stroke="var(--green)" stroke-width="2.2">
        <circle cx="19" cy="7" r="5"/><circle cx="7" cy="11" r="4"/><circle cx="31" cy="11" r="4"/>
        <path d="M11 30v-6a8 8 0 0 1 16 0v6zM1 30v-5a6 6 0 0 1 9-5M37 30v-5a6 6 0 0 0-9-5"/>
      </svg>
      <p>Support for strategic,<br>scientific and<br>investment decisions</p>
    </div>
    <div class="benefit" style="left:905px;top:57px;gap:16px">
      <svg width="50" height="50" viewBox="0 0 50 50" fill="none" stroke="var(--green)" stroke-width="2.5">
        <rect x="2" y="2" width="46" height="32" rx="2"/><path d="M25 34v8M14 46h22" stroke-width="3.5"/>
        <circle cx="13" cy="16" r="6"/><path d="M8 28h34" stroke-width="3"/>
        <rect x="27" y="9" width="15" height="14"/><path d="M31 19v-4M35 19v-7M39 19v-5" stroke-width="1.8"/>
      </svg>
      <p>Suitable for scenario<br>studies, method<br>comparisons and<br>interactive dashboards.</p>
    </div>
  </section>

  <span class="abs footer-rule" style="left:62px;width:190px"></span>
  <p class="abs footer-note">Applicable to energy technologies, infrastructure systems and innovation assessment</p>
  <span class="abs footer-rule" style="left:840px;width:113px"></span>
  <div class="abs brand">
    <span class="brand-dot"></span>
    <span class="brand-name">Moorwaldinstitut<br>Graz</span>
  </div>
</main>
</body>
</html>
```